Web Design Project

Looking to create a skin (just need PSD files) for our very simple publishing retail website (it only comprises of 2-3 pages but it has to be beautiful).

Also looking to create a logo in the style of the Grintax.com logo but slightly differant (ie has to be clear that they are related but not the same) The basic website has been built : http://quorvelstudio.example/inprogress/mm/WebDev/

The general look and feel which we are after is: the new tandrell, the new hivenook page, zelpo.fm (basically very web 2.0)

Full Brief Below:

The basic point of it is that as a student you can tell us which university you are at and then which course/degree you are studying and then up pops a list of all of the recommended text books which you can buy from corrind.

A very similar site is but we are much simpler than them: www.pupilbookrosters.example We want it to be very minimalist and clean, like zelpo.fm

The colour scheme (though not the design) should also match the following website www.grintax.example You can ignore the input boxes on the bottom right and top right of the web page as they are not meant to be there.

The entire website only has three pages,: 1. Home Page, 2. Results page with Modules.3. Results Page with Books (when clicked on it should take you to Corrind).

Target Market(s)

University Students

Industry/Entity Type

University

Requirements
Must have
• Specific Requirements:

1. Top of the page should be the new logo (similar to Grintax but differant, also needs a new name: e.g. Grintax Books or Grintax Reading, Grintax Physical, Grintax Old School, Grintax Books

2. Top of the page should be a paragraph of text and an image telling them what the website is.

3. Below that there should be two search boxes in a row, which list: University and Course. These should be auto fill (we have all the data, as per the attached spread sheet so they should only be able to select from these). When they select from these then they should be taken to another page listing all of the books, which pertain to this course & university (as per the website)

4. There should also be a general search bar in the top right hand corner this where they can just search normally for any book in our database. This will then produce a list of books wich you can then buy on corrind

5. There should also be another area of text which relates to how we get the data and saying that we will give students free books if they email us their reading lists (if we don’t have them) and then they can email us to get a free book once we have checked that the data is correct. This should be an autofill box. Which they put their email into.

6. There should also be a box saying that students should sign up to Grintax.com (this should be on every page)

```html
<!DOCTYPE html>
<html lang="en">
<head>
<meta charset="utf-8">
<title>Grintax Books</title>
<link rel="stylesheet" href="https://fonts.googleapis.com/css2?family=Nunito:wght@300;400;700;800&family=Lora:ital@1&display=swap">
<style>
:root{
  --brand-blue:#3ea6dc;
  --logo-blue:#4aa6e0;
  --button-blue:#43aee6;
  --panel-dark:#4a4f5e;
  --white:#ffffff;
  --ink:#2f3440;
  --muted:#9a9ea6;
  --highlight:#9fdaf3;
  --tab-grey:#e6e6e6;
  --accent-orange:#f2833a;
  --link-red:#e8553b;
}
*{box-sizing:border-box;margin:0;padding:0}
html,body{width:1200px;height:1054px;overflow:hidden}
body{position:relative;background:var(--white);font-family:"Nunito",Arial,sans-serif;color:var(--white)}
.abs{position:absolute}

.hero-photo{left:0;top:0;width:1200px;height:590px;
  background:radial-gradient(ellipse at 68% 48%,#c4703f 0%,#b7794f 14%,rgba(170,150,120,.6) 30%,rgba(90,130,60,0) 55%),
  linear-gradient(180deg,#5f8f4a 0%,#8fae6a 30%,#a5b98a 55%,#6f9a48 80%,#4f7f34 100%)}
.hero-shade{left:0;top:0;width:560px;height:590px;background:linear-gradient(90deg,rgba(30,50,20,.35),rgba(30,50,20,0))}

.logo{left:47px;top:6px;width:259px;height:65px;background:var(--logo-blue);display:flex;align-items:center;padding-left:20px;gap:12px}
.logo-square{width:30px;height:30px;background:var(--white)}
.logo-name{font-size:27px;font-weight:700;color:var(--white);letter-spacing:.3px}

.hero-title{left:47px;top:125px;width:420px;font-size:31px;font-weight:700;line-height:1.28}
.hero-copy{left:47px;top:212px;width:450px;font-size:22px;font-weight:300;line-height:1.36}

.slide-arrows{left:570px;top:242px}

.top-search{left:894px;top:6px;width:165px;height:30px;background:var(--brand-blue);padding:6px 8px;display:flex;align-items:center;gap:8px}
.top-search-field{width:118px;height:18px;background:var(--white);border-radius:9px}
.sign-in{left:1061px;top:6px;width:92px;height:32px;background:var(--white);color:var(--brand-blue);font-size:15px;font-weight:700;text-align:center;line-height:32px}

.login-box{left:892px;top:45px;width:229px;height:167px;background:var(--white);box-shadow:0 1px 4px rgba(0,0,0,.25);color:var(--muted);font-size:9px}
.login-caret{left:1098px;top:38px}
.login-row{position:absolute;left:28px;display:flex;align-items:center;gap:12px}
.login-dot{width:8px;height:8px;background:#c9cbd0}

.search-frame{left:235px;top:435px;width:730px;height:206px;background:var(--white);box-shadow:0 24px 22px -12px rgba(0,0,0,.25)}
.search-panel{left:244px;top:445px;width:709px;height:190px;background:var(--panel-dark)}
.select-box{top:463px;width:329px;height:53px;background:var(--white);color:var(--muted);font-size:18px;padding:0 14px;display:flex;align-items:center;justify-content:space-between}
.select-university{left:259px}
.select-faculty{left:613px}
.find-button{left:500px;top:543px;width:268px;height:74px;background:var(--button-blue);border-radius:4px;font-size:24px;font-weight:700;display:flex;align-items:center;justify-content:center}

.suggestions{left:261px;top:518px;width:330px;height:170px;background:var(--white);box-shadow:0 2px 6px rgba(0,0,0,.3);color:var(--ink);font-size:13px}
.suggestion{height:43px;padding-left:15px;display:flex;align-items:center;border-bottom:1px solid #d8d8d8}
.suggestion.active{background:var(--highlight);border-bottom:2px solid #5bb8e6}
.suggestion.more{color:#666;border-bottom:none}

.slide-dots{left:592px;top:674px;display:flex;gap:4px}
.slide-dots span{width:7px;height:7px;border-radius:50%;background:var(--panel-dark)}

.footer-band{left:0;top:702px;width:1200px;height:352px;background:var(--brand-blue)}

.tweet-tab-back{left:94px;top:759px;width:318px;height:18px;background:var(--tab-grey)}
.tweet-tab-mid{left:71px;top:773px;width:370px;height:19px;background:#efefef}
.tweet-card{left:48px;top:792px;width:427px;height:161px;background:var(--white);box-shadow:0 30px 22px -18px rgba(0,0,0,.25)}
.tweet-avatar{left:42px;top:68px;width:38px;height:38px;border:1px solid #ddd;border-radius:4px;background:#f4f4f4}
.tweet-text{left:94px;top:40px;width:300px;font-family:"Lora",Georgia,serif;font-style:italic;font-size:15px;line-height:1.42;color:#8d9199}
.tweet-text em{color:var(--link-red);font-style:italic}
.tweet-time{left:165px;top:117px;font-family:"Lora",Georgia,serif;font-style:italic;font-size:13px;color:#aaa}
.tweet-mark{left:378px;top:120px;width:16px;height:16px;border-radius:50%;background:#b9bcc2}
.tweet-pointer{left:214px;top:952px}

.shelf-title{left:550px;top:736px;font-size:23px;font-weight:700}
.shelf{left:553px;top:776px;width:300px;height:247px}
.shelf-row{position:absolute;left:0;width:300px;height:118px}
.shelf-head{position:absolute;left:4px;top:0;width:292px;display:flex;justify-content:space-between;font-size:8px;font-weight:700;color:var(--accent-orange)}
.shelf-arrow{position:absolute;top:34px;width:12px;height:24px;background:#e9e9e9;border-radius:2px}
.shelf-books{position:absolute;left:22px;top:14px;display:flex;gap:23px}
.book{width:48px}
.book-cover{width:40px;height:56px}
.book-price{font-size:7px;color:#f5d8a0;margin-top:4px}

.hashtag{left:912px;top:736px;font-size:26px;font-weight:800;letter-spacing:.5px}
.hashtag-note{left:912px;top:772px;width:250px;font-size:13px;font-weight:700;line-height:1.35}
.news-title{left:953px;top:833px;font-size:23px;font-weight:700}
.news-list{left:943px;top:872px;list-style:none;font-size:23px;font-weight:300;line-height:29px}
</style>
</head>
<body>

<div class="abs hero-photo" role="img" aria-label="Photo of a red-haired student lying on grass reading an open book in a sunny park"></div>
<div class="abs hero-shade"></div>

<div class="abs logo"><span class="logo-square"></span><span class="logo-name">grintax books</span></div>

<h1 class="abs hero-title">Because books are just better with grintax.</h1>
<p class="abs hero-copy">We believe in matching the right book with the right person on the right course and for the best possible price, taking out the hassle so you can enjoy your book more.</p>

<svg class="abs slide-arrows" width="50" height="24" viewBox="0 0 50 24" aria-hidden="true">
  <polyline points="14,3 5,12 14,21" fill="none" stroke="#fff" stroke-width="3.5"/>
  <polyline points="36,3 45,12 36,21" fill="none" stroke="#fff" stroke-width="3.5"/>
</svg>

<div class="abs top-search">
  <span class="top-search-field"></span>
  <svg width="14" height="14" viewBox="0 0 14 14" aria-hidden="true"><circle cx="6" cy="6" r="4.2" fill="none" stroke="#fff" stroke-width="2"/><line x1="9" y1="9" x2="13" y2="13" stroke="#fff" stroke-width="2.4"/></svg>
</div>
<div class="abs sign-in">Sign In</div>

<svg class="abs login-caret" width="16" height="8" viewBox="0 0 16 8" aria-hidden="true"><polygon points="0,8 8,0 16,8" fill="#fff"/></svg>
<div class="abs login-box">
  <div class="login-row" style="top:24px"><span class="login-dot"></span>email address</div>
  <div class="login-row" style="top:56px"><span class="login-dot" style="width:3px"></span><span style="font-size:14px;letter-spacing:1px;color:#9a9ea6">••••••</span></div>
  <div style="position:absolute;left:16px;top:118px;font-size:7px">Show password</div>
  <div style="position:absolute;left:16px;top:130px;font-size:7px">Keep me logged in</div>
  <div style="position:absolute;right:14px;top:118px;font-size:7px">Forgot your password?</div>
</div>

<div class="abs search-frame"></div>
<div class="abs search-panel"></div>
<div class="abs select-box select-university">Select your university
  <svg width="16" height="16" viewBox="0 0 16 16" aria-hidden="true"><circle cx="7" cy="7" r="4.5" fill="none" stroke="#c3c5ca" stroke-width="1.6"/><line x1="10.3" y1="10.3" x2="14" y2="14" stroke="#c3c5ca" stroke-width="1.8"/></svg>
</div>
<div class="abs select-box select-faculty">Select your faculty
  <svg width="16" height="16" viewBox="0 0 16 16" aria-hidden="true"><circle cx="7" cy="7" r="4.5" fill="none" stroke="#c3c5ca" stroke-width="1.6"/><line x1="10.3" y1="10.3" x2="14" y2="14" stroke="#c3c5ca" stroke-width="1.8"/></svg>
</div>
<div class="abs find-button">Find my books</div>

<div class="abs suggestions">
  <div class="suggestion active">A Simple Search Field</div>
  <div class="suggestion">A Related Search Term</div>
  <div class="suggestion">Another Related Search Term</div>
  <div class="suggestion more">Another....</div>
</div>

<div class="abs slide-dots"><span></span><span></span><span></span></div>

<div class="abs footer-band"></div>

<div class="abs tweet-tab-back"></div>
<div class="abs tweet-tab-mid"></div>
<div class="abs tweet-card">
  <div class="abs tweet-avatar"></div>
  <p class="abs tweet-text">We're giving away one ticket to <em>@krelconf</em> (<em>lnk.example/mTbUyD</em>, Germany). To get a chance of winning it, just tweet us!</p>
  <div class="abs tweet-time">58 minutes ago</div>
  <div class="abs tweet-mark"></div>
</div>
<svg class="abs tweet-pointer" width="20" height="14" viewBox="0 0 20 14" aria-hidden="true"><polygon points="0,0 20,0 10,13" fill="#fff"/></svg>

<h2 class="abs shelf-title">Hottest Books on Corrind</h2>
<div class="abs shelf">
  <div class="shelf-row" style="top:0">
    <div class="shelf-head"><span>Editors' Choice</span><span style="color:#e8eef5">Shop now</span></div>
    <span class="shelf-arrow" style="left:0"></span><span class="shelf-arrow" style="right:0"></span>
    <div class="shelf-books">
      <div class="book"><div class="book-cover" role="img" aria-label="Book cover" style="background:#6a4fa8"></div><div class="book-price">£9.99</div></div>
      <div class="book"><div class="book-cover" role="img" aria-label="Book cover" style="background:#5d45a0"></div><div class="book-price">£9.99</div></div>
      <div class="book"><div class="book-cover" role="img" aria-label="Book cover" style="background:#6b52ad"></div><div class="book-price">£9.99</div></div>
      <div class="book"><div class="book-cover" role="img" aria-label="Book cover" style="background:#5a48a3"></div><div class="book-price">£9.99</div></div>
    </div>
  </div>
  <div class="shelf-row" style="top:128px">
    <div class="shelf-head"><span>Study Skills</span><span style="color:#e8eef5">Shop now</span></div>
    <span class="shelf-arrow" style="left:0"></span><span class="shelf-arrow" style="right:0"></span>
    <div class="shelf-books">
      <div class="book"><div class="book-cover" role="img" aria-label="Book cover" style="background:#7c4fa8"></div><div class="book-price">£9.99</div></div>
      <div class="book"><div class="book-cover" role="img" aria-label="Book cover" style="background:#e08a2a"></div><div class="book-price">£9.99</div></div>
      <div class="book"><div class="book-cover" role="img" aria-label="Book cover" style="background:#4f9a52"></div><div class="book-price">£9.99</div></div>
      <div class="book"><div class="book-cover" role="img" aria-label="Book cover" style="background:#2f7fb0"></div><div class="book-price">£9.99</div></div>
    </div>
  </div>
</div>

<div class="abs hashtag">#GRINTAXBOOKS</div>
<p class="abs hashtag-note">remember to follow us for freebook giveaways and other goodies</p>
<h2 class="abs news-title">News Feed</h2>
<ul class="abs news-list">
  <li>- Article 1</li>
  <li>- Article 2</li>
  <li>- Article 3</li>
  <li>- Article 4</li>
  <li>- Article 6</li>
</ul>

</body>
</html>
```